Financial Advisor needs a NEW business card design

We need a new card design as our current design has no white space and clients tend to want to write on the card. I am attaching our current logos and current card design. I have also played with some designs I liked online but don't have the knowledge (or software) to complete the designs in a format that is appropriate for production. I've attached those designs that I liked too. With two office locations and a disclaimer there is a lot of info but we want it to look tidy. We like the deep, rich blue colors and want it to look clean, strong, and modern yet classic.
Business
Included in the attached files

```html
<!DOCTYPE html>
<html lang="en">
<head>
<meta charset="utf-8">
<title>Harlow Financial Advisory – Business Card</title>
<link href="https://fonts.googleapis.com/css2?family=Cinzel:wght@400;600&display=swap" rel="stylesheet">
<style>
  :root {
    --navy: #0d2d4d;
    --navy-text: #16324f;
    --paper: #f1f1ef;
    --stage: #8a8c8e;
    --light: #e9ecef;
  }
  * { margin: 0; padding: 0; box-sizing: border-box; }
  html, body { width: 1200px; height: 1029px; overflow: hidden; }
  body {
    background: var(--stage);
    font-family: "Cinzel", Georgia, serif;
    position: relative;
  }
  .card {
    position: absolute;
    left: 180px;
    width: 840px;
    height: 480px;
    background: var(--paper);
    overflow: hidden;
    box-shadow: 0 6px 18px rgba(0,0,0,0.25);
  }
  .card--back { top: 20px; }
  .card--front { top: 529px; }

  /* back */
  .back-band-top { position: absolute; left: 0; top: 0; width: 100%; height: 105px; background: var(--navy); }
  .back-band-bottom { position: absolute; left: 0; top: 265px; width: 100%; height: 215px; background: var(--navy); }
  .wordmark {
    position: absolute;
    display: flex;
    align-items: center;
    gap: 14px;
    color: var(--navy-text);
    font-weight: 600;
    letter-spacing: 1px;
  }
  .wordmark__square { width: 16px; height: 16px; background: var(--navy-text); }
  .card--back .wordmark { left: 0; right: 0; top: 162px; justify-content: center; font-size: 30px; }
  .disclaimer {
    position: absolute;
    left: 130px; right: 130px; top: 300px;
    text-align: center;
    color: var(--light);
    font-size: 15px;
    line-height: 1.55;
    letter-spacing: 0.5px;
  }

  /* front */
  .front-band { position: absolute; left: 0; top: 330px; width: 100%; height: 150px; background: var(--navy); }
  .holder { position: absolute; left: 62px; top: 62px; color: var(--navy-text); }
  .holder__name { font-size: 30px; font-weight: 600; letter-spacing: 1px; }
  .holder__title { font-size: 14px; letter-spacing: 1.5px; margin-top: 2px; padding-left: 18px; color: #4a5a6a; }
  .card--front .wordmark { right: 70px; top: 108px; font-size: 27px; }

  .contact { position: absolute; left: 62px; display: flex; align-items: flex-start; gap: 22px; color: #2a2f36; font-size: 15px; line-height: 1.45; letter-spacing: 0.5px; }
  .contact--phone { top: 196px; }
  .contact--web { top: 256px; }
  .icon { width: 30px; height: 30px; flex: none; }
  .address { position: absolute; top: 372px; display: flex; gap: 22px; color: var(--light); font-size: 15px; line-height: 1.45; letter-spacing: 0.5px; }
  .address--fw { left: 62px; }
  .address--plano { left: 450px; top: 392px; }
</style>
</head>
<body>

<section class="card card--back" aria-label="Card back">
  <div class="back-band-top"></div>
  <div class="wordmark"><span class="wordmark__square"></span>Harlow Financial Advisory</div>
  <div class="back-band-bottom"></div>
  <p class="disclaimer">Investment advisory services offered through Northpoint Private Capital, LLC, an SEC registered investment advisor.</p>
</section>

<section class="card card--front" aria-label="Card front">
  <div class="holder">
    <div class="holder__name">Daniel Marlowe</div>
    <div class="holder__title">Financial Advisor</div>
  </div>

  <div class="wordmark"><span class="wordmark__square"></span>Harlow Financial Advisory</div>

  <div class="contact contact--phone">
    <svg class="icon" viewBox="0 0 30 30" aria-hidden="true">
      <rect x="1.5" y="1.5" width="27" height="27" rx="3" fill="none" stroke="#16324f" stroke-width="2"/>
      <path d="M10 8 l3 0 l1.5 4 l-2 1.5 q1.5 3 4 4 l1.5 -2 l4 1.5 l0 3 q-1 1.5 -3 1.5 q-9 -1.5 -10.5 -10.5 q0 -2 1.5 -3 z" fill="#16324f"/>
    </svg>
    <div>(Fort Worth) 817.555.0142<br>(Plano) 972.555.0187</div>
  </div>

  <div class="contact contact--web">
    <svg class="icon" viewBox="0 0 30 30" aria-hidden="true">
      <rect x="1.5" y="1.5" width="27" height="27" rx="3" fill="none" stroke="#16324f" stroke-width="2"/>
      <circle cx="15" cy="15" r="7" fill="#16324f"/>
    </svg>
    <div>daniel@harlowfinancial.com<br>www.harlowfinancial.com</div>
  </div>

  <div class="front-band"></div>

  <div class="address address--fw">
    <svg class="icon" viewBox="0 0 30 30" aria-hidden="true">
      <rect x="1.5" y="1.5" width="27" height="27" rx="3" fill="none" stroke="#e9ecef" stroke-width="2"/>
      <path d="M15 7 a5 5 0 0 1 5 5 q0 4 -5 10 q-5 -6 -5 -10 a5 5 0 0 1 5 -5 z" fill="none" stroke="#e9ecef" stroke-width="1.8"/>
      <circle cx="15" cy="12" r="1.8" fill="#e9ecef"/>
    </svg>
    <div>2840 Mill Creek Road, Suite 210<br>Fort Worth, Texas 76112</div>
  </div>

  <div class="address address--plano">
    <svg class="icon" viewBox="0 0 30 30" aria-hidden="true">
      <rect x="1.5" y="1.5" width="27" height="27" rx="3" fill="none" stroke="#e9ecef" stroke-width="2"/>
      <path d="M15 7 a5 5 0 0 1 5 5 q0 4 -5 10 q-5 -6 -5 -10 a5 5 0 0 1 5 -5 z" fill="none" stroke="#e9ecef" stroke-width="1.8"/>
      <circle cx="15" cy="12" r="1.8" fill="#e9ecef"/>
    </svg>
    <div>450 Cedar Ridge Blvd, Suite 300<br>Plano, Texas 75074</div>
  </div>
</section>

</body>
</html>
```